Medicated Oil packaging design

We are looking for a new packaging design for our medicated oil, known as Calmera Balm.
- Plastic box packaging with inserts to hold the small bottle in place in the middle.
- Dimension of box is L 4cm x W 4 cm x H 8cm (Not fix, please recommend a better dimension if need be)
- The information in the word document to be displayed on 2 sides of the box.
- Selling point is the exquisite bottle, with convenient roller tip for easy application of the oil within.
-Product to target mass market, but should have a classy view/ up market outlook.
-Product to be displayed from top view and side view.
- Actual bottle is 6cm long (capped) and 1.5cm in diameter
Updates

Project Deadline Extended
Reason: Need to be overseas on a business trip, meanwhile extend the deadline since I cannot check submissions anyway.

Dear Deisgners,

Thank you for all your hard work so far. There are some wonderful designs that I would submit for voting, but a sudden new requirement came up that i need you cooperation.. I am very sorry about this. Therefore i am increasing the budget allocated for this. 

The new requirement is fairly straightforward, I have uploaded a new file called Dr photo, this person is a Chinese Physician who formulated the product. His name is Mr Lim Boon Teck. I need to include his photo on the product, as long as his face is shown will be adequate.

Meanwhile will be extending this project but a few days to cater to the new requirement. Sincere apologies and most gratitude for your hard work. Thanks a million!!

Project Deadline Extended
Reason: Added a new requirement, need to include the photo of the formulator of the product, Mr Lim Boon Teck, onto the product. See upload for the file 'Dr photo'. Also added more budget for this. Design away~ Thanks!

Target Market(s)

Mass market, to be sold at all sorts of pharmacies, convenience stores and newspaper stands.

Industry/Entity Type

Plastic

Requirements
Must have
• Must have all the wordings in the attached word document.
Make it clear that it is medicated oil, not perfume or other products.

Provide an 'insert design' for the plastic to hold the bottle in the middle of the box.
Nice to have
• Convey messages of soothing relaxation after application.
Should not have
• Nothing i can think of yet =)

```html
<!DOCTYPE html>
<html lang="en">
<head>
<meta charset="utf-8">
<title>Calmera Balm – Box Dieline</title>
<link rel="stylesheet" href="https://fonts.googleapis.com/css2?family=Arimo:wght@400;700&family=Cinzel:wght@500&display=swap">
<style>
  :root {
    --paper: #ffffff;
    --panel: #f1f1f1;
    --line: #3a3a3a;
    --orange: #f26a1b;
    --frame: #f39a3c;
    --green: #1f6b3a;
    --leaf: #2c6e3c;
    --bark: #7a5a2e;
    --ink: #1a1a1a;
    --brand: #7a6a5a;
  }
  * { margin: 0; padding: 0; box-sizing: border-box; }
  html, body { width: 1200px; height: 848px; overflow: hidden; background: var(--paper); }
  .canvas { position: relative; width: 1200px; height: 848px; font-family: "Arimo", Arial, sans-serif; color: var(--ink); }
  .dieline { position: absolute; inset: 0; }
  .dieline .cut { fill: var(--paper); stroke: var(--line); stroke-width: 1; }
  .dieline .face { fill: var(--panel); stroke: var(--line); stroke-width: 1; }
  .brand {
    position: absolute; font-family: "Cinzel", serif; font-weight: 500;
    font-size: 17px; letter-spacing: 1px; color: var(--brand); text-align: center; width: 140px;
  }
  .brand-mark { display: block; width: 12px; height: 12px; border-radius: 50%; background: var(--leaf); margin: 0 auto 4px; }
  .product-name {
    position: absolute; width: 162px; text-align: center;
    font-weight: 700; font-size: 15px; color: var(--orange); letter-spacing: 0.2px;
  }
  .bottle-window {
    position: absolute; width: 137px; height: 226px;
    border: 1.5px solid var(--frame); border-radius: 6px; overflow: hidden;
    background: linear-gradient(155deg, var(--panel) 45%, #cfdcc9 70%, var(--leaf) 88%, var(--bark) 100%);
  }
  .volume { position: absolute; width: 162px; text-align: center; font-weight: 700; font-size: 10px; color: var(--orange); }
  .info { position: absolute; left: 487px; top: 347px; width: 128px; font-size: 7.6px; line-height: 10px; }
  .info .label {
    display: inline-block; background: var(--green); color: #fff; font-weight: 700;
    font-size: 9.5px; padding: 0 2px; line-height: 12px; letter-spacing: 0.3px;
  }
  .info p { margin: 7px 0 4px; }
  .glue-mark { position: absolute; left: 468px; top: 447px; width: 18px; height: 43px; background: var(--ink); }
  .lid-brand { left: 638px; top: 206px; transform: rotate(180deg); }
  .formulator-photo {
    position: absolute; left: 808px; top: 348px; width: 51px; height: 64px;
    border: 1px solid #999; background: linear-gradient(180deg, #e9ecef, #b9c3cc);
  }
  .back { position: absolute; left: 809px; width: 130px; font-weight: 700; font-size: 9.5px; line-height: 13px; }
</style>
</head>
<body>
<div class="canvas">
  <svg class="dieline" width="1200" height="848" viewBox="0 0 1200 848" aria-hidden="true">
    <!-- glue flap -->
    <path class="cut" d="M306 305 L256 313 Q248 315 248 323 L248 565 L306 623 Z"/>
    <!-- top dust flaps -->
    <path class="cut" d="M469 305 L469 292 L482 286 L482 236 Q482 225 493 225 L603 225 Q614 225 614 236 L614 286 L628 292 L628 305 Z"/>
    <path class="cut" d="M793 305 L793 292 L806 286 L806 236 Q806 225 817 225 L927 225 Q938 225 938 236 L938 286 L950 292 L950 305 Z"/>
    <!-- lid with tuck -->
    <path class="cut" d="M630 305 L630 165 Q630 155 642 152 L690 146 L660 146 Q632 146 632 122 Q632 95 660 95 L762 95 Q790 95 790 122 Q790 146 762 146 L732 146 L780 152 Q792 155 792 165 L792 305 Z"/>
    <!-- bottom flaps -->
    <path class="cut" d="M306 628 L318 640 L318 745 Q318 752 326 752 L355 752 L398 710 L440 747 L455 747 Q460 747 460 740 L460 640 L468 628 Z"/>
    <path class="cut" d="M468 628 L482 640 L548 698 L614 640 L630 628 Z"/>
    <path class="cut" d="M630 628 L642 640 L642 745 Q642 752 650 752 L690 752 L735 708 L760 745 L777 745 Q782 745 782 738 L782 640 L792 628 Z"/>
    <path class="cut" d="M792 628 L806 640 L872 698 L934 640 L946 628 Z"/>
    <!-- main faces -->
    <rect class="face" x="306" y="305" width="162" height="323"/>
    <rect class="face" x="468" y="305" width="162" height="323"/>
    <rect class="face" x="630" y="305" width="162" height="323"/>
    <rect class="face" x="792" y="305" width="154" height="323"/>
    <rect class="face" x="630" y="165" width="162" height="140" style="fill:var(--panel)"/>
  </svg>

  <!-- front panel -->
  <div class="brand" style="left:317px;top:322px;"><span class="brand-mark"></span>ARBORIA</div>
  <div class="product-name" style="left:306px;top:366px;">CALMERA BALM</div>
  <div class="bottle-window" style="left:318px;top:388px;" role="img" aria-label="Green tree with brown trunk rising from the lower right corner"></div>
  <div class="volume" style="left:306px;top:617px;">5ML</div>

  <!-- information panel -->
  <div class="glue-mark"></div>
  <div class="info">
    <span class="label">INDICATIONS:</span>
    <p>Relief for headaches, giddiness, itch, runny nose and tummy-aches.</p>
    <span class="label">DIRECTIONS:</span>
    <p>Apply to skin, massage gently as needed. Or inhale from a fabric or tissue paper after tapping with a few drips of Soothing Fluid.</p>
    <span class="label">CAUTION:</span>
    <p>For external use only. Not to be administered orally. Do not apply onto open wounds or to damaged skin. Avoid contact with eyes or on mucous membranes. Keep out of reach of children.</p>
    <span class="label">COMPOSITION:</span>
    <p>Wintergreen Oil- 35%, Eucalyptus Oil-25%, Menthol-20%, White Oil-20%</p>
  </div>

  <!-- second front panel -->
  <div class="brand" style="left:641px;top:322px;"><span class="brand-mark"></span>ARBORIA</div>
  <div class="product-name" style="left:630px;top:366px;">CALMERA BALM</div>
  <div class="bottle-window" style="left:641px;top:387px;" role="img" aria-label="Green tree with brown trunk rising from the lower right corner"></div>
  <div class="volume" style="left:630px;top:617px;">5ML</div>

  <!-- lid -->
  <div class="brand lid-brand"><span class="brand-mark"></span>ARBORIA</div>

  <!-- back panel -->
  <div class="formulator-photo" role="img" aria-label="Portrait photo of the product formulator"></div>
  <div class="back" style="top:418px;">The formulator of the product,<br>“Mr Lim Boon Teck”</div>
  <div class="back" style="top:453px;">Made in Singapore</div>
  <div class="back" style="top:470px;">MANUFACTURED BY:<br>ARBORIA PRIVATE LIMITED</div>
  <div class="back" style="top:517px;">Mfg. Date:</div>
  <div class="back" style="top:550px;">Exp. Date:</div>
  <div class="back" style="top:583px;">Batch No.:</div>
</div>
</body>
</html>
```